Legal Service Estimated Retainer and Average Case Value

We need an 11x14 flyer that contains the standard retainers and average cost be case, both provided in documents, for each case type we handle. We need the information displayed, preferably in a way that makes the information readable but less troubling to a client shocked at price of litigation. We need one sheet with the retainers and average case value merged into one table.

Target Market(s)

Potential Clients

Font styles to use
Serif
Sans Serif

```html
<!DOCTYPE html>
<html lang="en">
<head>
<meta charset="utf-8">
<title>Average Fee Per Case Type — Law Office of Marcus T Whitfield</title>
<link href="https://fonts.googleapis.com/css2?family=EB+Garamond:wght@400;500;600&display=swap" rel="stylesheet">
<style>
  :root {
    --backdrop: #4a4a4a;
    --navy-top: #0f1c5c;
    --navy-mid: #0a1548;
    --navy-deep: #060e36;
    --rule: #c9cfe0;
    --ink: #ffffff;
    --ink-soft: #e6e9f2;
  }
  * { box-sizing: border-box; margin: 0; padding: 0; }
  html, body {
    width: 1200px; height: 800px; overflow: hidden;
    background: var(--backdrop);
    font-family: "EB Garamond", Georgia, serif;
  }
  .flyer {
    position: absolute; left: 320px; top: 20px;
    width: 560px; height: 760px;
    background: linear-gradient(180deg, var(--navy-mid) 0%, var(--navy-deep) 55%, var(--navy-mid) 100%);
    color: var(--ink);
    overflow: hidden;
  }
  .masthead {
    height: 120px;
    display: flex; align-items: center;
    padding: 0 20px 0 26px;
    background: linear-gradient(180deg, var(--navy-top) 0%, var(--navy-deep) 100%);
  }
  .masthead-copy { width: 290px; }
  .title {
    font-size: 16.5px; font-weight: 500; letter-spacing: 2.6px;
    text-transform: uppercase; margin-bottom: 10px;
  }
  .intro { font-size: 9px; line-height: 1.45; color: var(--ink-soft); letter-spacing: -0.1px; }
  .divider { width: 1px; height: 82px; background: var(--rule); margin: 0 20px; opacity: .8; }
  .firm { display: flex; align-items: center; gap: 8px; }
  .firm-mark { width: 30px; height: 30px; border: 2px solid var(--ink); }
  .firm-name { font-size: 14.5px; font-weight: 500; line-height: 1.05; text-transform: uppercase; }
  .firm-name small { display: block; font-size: 7px; letter-spacing: .3px; }

  .fee-table { width: 100%; border-collapse: collapse; }
  .fee-table td {
    height: 22px; font-size: 13.2px; line-height: 1;
    border-top: 1.5px solid var(--rule); vertical-align: middle;
  }
  .fee-table .case { padding-left: 24px; }
  .fee-table .amount { width: 160px; text-align: left; padding-left: 22px; }
  .section-head td {
    height: 34px; border-top: 1.5px solid var(--rule);
    text-align: center; font-size: 15px; font-weight: 500;
    letter-spacing: 2.4px; text-transform: uppercase;
  }
  .retainers .case-strong { font-weight: 500; }
  .closing-rules { border-top: 1.5px solid var(--rule); }
  .closing-rules span { display: block; height: 4px; border-bottom: 1px solid var(--rule); }
</style>
</head>
<body>
  <article class="flyer">
    <header class="masthead">
      <div class="masthead-copy">
        <h1 class="title">Average Fee Per Case Type</h1>
        <p class="intro">In order for our clients to set expectations for legal fees, we provide the national average range of fees per case type. These are only to provide you with an understanding of what other cases have cost clients in similar cases. Please note these are not estimates nor guarantees of your own legal costs.</p>
      </div>
      <div class="divider"></div>
      <div class="firm">
        <span class="firm-mark"></span>
        <p class="firm-name"><small>The Law Office of</small>Marcus T Whitfield</p>
      </div>
    </header>

    <table class="fee-table averages">
      <tr><td class="case">Custody Contempt/Modification</td><td class="amount">$5,000 - $8,000</td></tr>
      <tr><td class="case">Custody Initial Order</td><td class="amount">$4,000 - $7,000</td></tr>
      <tr><td class="case">Custody &amp; Support</td><td class="amount">$5,000 - $8,000</td></tr>
      <tr><td class="case">Support</td><td class="amount">$2,000 - $4,000</td></tr>
      <tr><td class="case">Divorce (3301c)</td><td class="amount">$1,500 - $3,000</td></tr>
      <tr><td class="case">Divorce (3301d)</td><td class="amount">$2,000 - $3,000</td></tr>
      <tr><td class="case">Protection from Abuse</td><td class="amount">$1,500 - $3,000</td></tr>
      <tr><td class="case">Divorce &amp; Custody</td><td class="amount">$5,000 - $8,000</td></tr>
      <tr><td class="case">Divorce &amp; Equitable Distribution</td><td class="amount">$6,000 - $10,000</td></tr>
      <tr><td class="case">Divorce, Custody &amp; Support</td><td class="amount">$8,000 - $12,000</td></tr>
      <tr><td class="case">Divorce, Equitable Distribution &amp; Custody</td><td class="amount">$10,000 - $15,000</td></tr>
      <tr><td class="case">Divorce, Equitable Distribution &amp; Support</td><td class="amount">$8,000 - $12,000</td></tr>
      <tr><td class="case">Divorce, Equitable Distribution, Custody &amp; Support</td><td class="amount">$12,000 - $15,000</td></tr>
      <tr class="section-head"><td colspan="2">Retainers and Total Estimated Case Costs</td></tr>
    </table>
    <table class="fee-table retainers">
      <tr><td class="case">Divorce (3301 C)</td><td class="amount">Retainer: $2,000</td></tr>
      <tr><td class="case">Divorce (3301 D)</td><td class="amount">Retainer: $2,500</td></tr>
      <tr><td class="case">Divorce and Custody</td><td class="amount">Retainer: $3,500</td></tr>
      <tr><td class="case">Divorce and Equitable Distribution</td><td class="amount">Retainer: $3,500</td></tr>
      <tr><td class="case">Divorce and Support</td><td class="amount">Retainer: $3,000</td></tr>
      <tr><td class="case">Divorce, Custody and Support</td><td class="amount">Retainer: $4,000</td></tr>
      <tr><td class="case">Divorce, Equitable Distribution and Support</td><td class="amount">Retainer: $4,000</td></tr>
      <tr><td class="case">Divorce, Equitable Distribution and Custody</td><td class="amount">Retainer: $4,500</td></tr>
      <tr><td class="case">Divorce, Equitable Distribution, Custody and Support</td><td class="amount">Retainer: $5,000</td></tr>
      <tr><td class="case case-strong">Custody Initial Order</td><td class="amount">Retainer: $3,000</td></tr>
      <tr><td class="case case-strong">Custody Modification</td><td class="amount">Retainer: $3,000</td></tr>
      <tr><td class="case case-strong">Custody and Support</td><td class="amount">Retainer: $3,500</td></tr>
      <tr><td class="case case-strong">(PFA) Protection From Abuse</td><td class="amount">Retainer: $1,500</td></tr>
    </table>
    <div class="closing-rules"><span></span><span></span></div>
  </article>
</body>
</html>
```